VelloPath Business Card

Our company is called VelloPath and we are based in Tel Aviv, Israel. We create innovative and exciting methods for getting people on the web engaged with content. We need a cool yet professional business card that will represent our management level employees. keep in mind this is a start up company with a young atmosphere. You can be inspired by our logo (file attached, make sure you have the right font "Ubuntu-Condensed") Use the colors that are used in the logo and create a colourful and professional business card.

```html
<!DOCTYPE html>
<html lang="en">
<head>
<meta charset="utf-8">
<title>VelloPath Business Card</title>
<link rel="stylesheet" href="https://fonts.googleapis.com/css2?family=Ubuntu+Condensed&family=Ubuntu:wght@400&display=swap">
<style>
  :root {
    --backdrop: #ecebe8;
    --card: #ffffff;
    --ink: #222226;
    --brand-blue: #2089cc;
    --panel-grey: #e5e5e7;
    --pink: #ea1d7c;
    --orange: #f8a83a;
    --yellow: #fdd11a;
    --green: #8bc540;
    --contact-ink: #1e1e22;
  }
  * { box-sizing: border-box; margin: 0; padding: 0; }
  html, body {
    width: 1200px; height: 900px; overflow: hidden;
    background: var(--backdrop);
  }
  .card {
    position: absolute; left: 100px; top: 164px;
    width: 1000px; height: 571px;
    background: var(--card);
    box-shadow: 0 6px 24px rgba(0,0,0,0.12);
    overflow: hidden;
  }
  .card-bands { position: absolute; inset: 0; }
  .brand {
    position: absolute; left: 96px; top: 130px;
    display: flex; align-items: center; gap: 16px;
  }
  .brand-dot {
    width: 26px; height: 26px; border-radius: 50%;
    background: var(--brand-blue);
  }
  .brand-name {
    font-family: "Ubuntu Condensed", "Arial Narrow", sans-serif;
    font-size: 70px; line-height: 1;
    color: var(--ink);
    letter-spacing: 1px;
  }
  .holder {
    position: absolute; left: 84px; top: 322px;
    color: #ffffff;
  }
  .holder-name {
    font-family: "Ubuntu Condensed", "Arial Narrow", sans-serif;
    font-size: 34px; line-height: 1.05;
    text-transform: uppercase;
  }
  .holder-role {
    font-family: "Ubuntu", sans-serif;
    font-size: 17px; margin-left: 26px;
  }
  .contact {
    position: absolute; right: 48px;
    font-family: "Ubuntu", sans-serif;
    font-size: 15px; line-height: 1.45;
    color: var(--contact-ink);
    text-align: right;
  }
  .contact-web { top: 378px; }
  .contact-phone { top: 432px; }
</style>
</head>
<body>
  <div class="card">
    <svg class="card-bands" width="1000" height="571" viewBox="0 0 1000 571" aria-hidden="true">
      <rect x="0" y="300" width="1000" height="55" fill="var(--panel-grey)"/>
      <rect x="0" y="366" width="1000" height="58" fill="var(--panel-grey)"/>
      <rect x="0" y="430" width="1000" height="48" fill="var(--panel-grey)"/>
      <polygon points="480,478 598,478 636,571 518,571" fill="var(--pink)"/>
      <polygon points="598,478 716,478 754,571 636,571" fill="var(--orange)"/>
      <polygon points="716,478 834,478 872,571 754,571" fill="var(--yellow)"/>
      <polygon points="834,478 1000,478 1000,571 872,571" fill="var(--green)"/>
      <polygon points="0,300 410,300 520,571 0,571" fill="var(--brand-blue)"/>
    </svg>

    <div class="brand">
      <span class="brand-name">VelloPath</span>
      <span class="brand-dot"></span>
    </div>

    <div class="holder">
      <p class="holder-name">Dario Fontana</p>
      <p class="holder-role">Graphic Designer</p>
    </div>

    <div class="contact contact-web">
      <p>admin@vellopath.co</p>
      <p>www.vellopath.co</p>
    </div>
    <div class="contact contact-phone">
      <p>000 - 4417 - 2093</p>
      <p>000 - 6352 - 8810</p>
    </div>
  </div>
</body>
</html>
```